RM Tomás Rivera (Business Card)

Hi designers, in this work, I'm looking for an sophisticated stylish, elegant and proffesional personal card. We have a laboratory of pathology automated, with equipments high quality.
In this web the designers, have created my business logo, the name is "RM Tomás Rivera"
In our lab, we principal work is to prepare the biopsies for further diagnostic of diseases like cancer, tumors, etc.
I need that the first face, only having my complete logo (Rm Tomás Rivera, Laboratorio de procesamiento Histologico)
The overleaf, could repeat the same logo, like water logo.
In this face, I need to say: My full data:

Técnico en Anatomía Patológica
Tomás Rivera Ibarra M.P 47203
Av. Paredes Luján 418 - 2do piso - Instituto Marbel.
Córdoba, Argentina
(0351) 154820937
rivera.tomas@correolab.example

with respect the colors of card, use your imagination, the original logo color is violet, I haven't chosen a color base for the card.

attached pictures are examples of cards I like your DESIGN.
Attached too, the original logo to my company.

the size of card are:
horizontal: 9cm
vertical: 5,5cm

any question that you have, not doubt to question me,
Hand to work!

Industry/Entity Type

Laboratory

Requirements
Must have
• designers sophisticated, not simples, like show the images attached

```html
<!DOCTYPE html>
<html lang="es">
<head>
<meta charset="utf-8">
<title>Tomás Rivera – Tarjeta personal</title>
<link rel="stylesheet" href="https://fonts.googleapis.com/css2?family=Raleway:wght@400;500&family=Ubuntu:wght@400;500;700&display=swap">
<style>
  :root {
    --violet: #8a3fb5;
    --violet-deep: #6b2a94;
    --ink: #141414;
    --grey-text: #6d6d6d;
    --card-white: #ffffff;
    --card-grey-top: #f4f4f4;
    --card-grey-bottom: #d9d9d9;
    --stage: #e9e7e4;
    --label-white: #fbfbfb;
    --band-text: #f2f2f2;
  }
  * { box-sizing: border-box; margin: 0; padding: 0; }
  html, body {
    width: 1200px; height: 1000px; overflow: hidden;
    background: var(--stage);
  }
  .stage {
    width: 1200px; height: 1000px;
    display: flex; flex-direction: column; align-items: center;
    justify-content: center; gap: 40px;
  }
  .card {
    width: 720px; height: 440px; position: relative; overflow: hidden;
    box-shadow: 0 6px 18px rgba(0,0,0,.18);
  }

  /* Front face */
  .card--front {
    background: var(--card-white);
    display: flex; flex-direction: column; align-items: center; justify-content: center;
  }
  .brand { display: flex; align-items: center; gap: 14px; }
  .brand__square { width: 22px; height: 22px; background: var(--violet); }
  .brand__name {
    font-family: "Raleway", sans-serif; font-weight: 500;
    font-size: 30px; letter-spacing: 8px; text-transform: uppercase;
    color: var(--violet);
  }
  .tagline {
    margin-top: 14px;
    font-family: "Raleway", sans-serif; font-weight: 400;
    font-size: 21px; letter-spacing: .5px; text-transform: uppercase;
    color: var(--grey-text);
  }

  /* Back face */
  .card--back {
    background: linear-gradient(160deg, var(--card-grey-top) 0%, var(--card-grey-bottom) 100%);
  }
  .watermark {
    position: absolute; left: 40px; top: 44px;
    display: flex; flex-direction: column; gap: 8px; opacity: .32;
  }
  .watermark .brand__name { color: #9a9a9a; font-size: 26px; }
  .watermark .brand__square { background: #9a9a9a; width: 18px; height: 18px; }
  .watermark .tagline { margin-top: 0; font-size: 19px; color: #8a8a8a; }

  .id-label {
    position: absolute; left: 40px; top: 170px;
    background: var(--label-white); padding: 12px 22px 12px 22px;
    box-shadow: 0 2px 6px rgba(0,0,0,.12);
  }
  .id-label__name {
    font-family: "Ubuntu", sans-serif; font-weight: 700;
    font-size: 31px; color: var(--violet); letter-spacing: .5px;
  }
  .id-label__title {
    font-family: "Ubuntu", sans-serif; font-weight: 500;
    font-size: 19px; color: var(--violet); margin-top: 2px; padding-left: 60px;
  }

  .accent-line { position: absolute; left: 0; right: 0; top: 282px; height: 6px; background: var(--violet); }
  .contact-band {
    position: absolute; left: 0; right: 0; top: 288px; bottom: 0;
    background: var(--ink);
    display: flex; justify-content: space-between; align-items: center;
    padding: 0 34px;
    font-family: "Ubuntu", sans-serif; font-weight: 500; color: var(--band-text);
  }
  .address { display: flex; align-items: flex-end; gap: 14px; font-size: 17px; line-height: 1.35; }
  .contact-list { display: flex; flex-direction: column; gap: 12px; font-size: 17px; }
  .contact-item { display: flex; align-items: center; gap: 12px; }
  .icon { width: 24px; height: 24px; flex: none; }
</style>
</head>
<body>
<main class="stage">

  <section class="card card--front" aria-label="Frente de la tarjeta">
    <div class="brand">
      <span class="brand__square"></span>
      <span class="brand__name">RM Tomás Rivera</span>
    </div>
    <p class="tagline">Laboratorio de Procesamiento Histologico</p>
  </section>

  <section class="card card--back" aria-label="Dorso de la tarjeta">
    <div class="watermark" aria-hidden="true">
      <div class="brand">
        <span class="brand__square"></span>
        <span class="brand__name">RM Tomás Rivera</span>
      </div>
      <p class="tagline">Laboratorio de Procesamiento Histologico</p>
    </div>

    <div class="id-label">
      <p class="id-label__name">Tomás Rivera Ibarra M.P 47203</p>
      <p class="id-label__title">Técnico en Anatomía Patológica</p>
    </div>

    <div class="accent-line"></div>

    <div class="contact-band">
      <div class="address">
        <svg class="icon" viewBox="0 0 24 24" aria-hidden="true">
          <path d="M12 3 L2 12 H5 V21 H10 V15 H14 V21 H19 V12 H22 Z" fill="#f2f2f2"/>
        </svg>
        <p>Av. Paredes Luján 418 - 2do piso<br>Instituto Marbel.<br>Córdoba, Argentina</p>
      </div>
      <div class="contact-list">
        <p class="contact-item">
          <svg class="icon" viewBox="0 0 24 24" aria-hidden="true">
            <rect x="6" y="2" width="12" height="20" rx="2" fill="none" stroke="#f2f2f2" stroke-width="2"/>
            <line x1="10" y1="18.5" x2="14" y2="18.5" stroke="#f2f2f2" stroke-width="1.6"/>
          </svg>
          (0351) 154820937
        </p>
        <p class="contact-item">
          <svg class="icon" viewBox="0 0 24 24" aria-hidden="true">
            <rect x="2" y="5" width="20" height="14" fill="#f2f2f2"/>
            <path d="M2 5 L12 13 L22 5" fill="none" stroke="#141414" stroke-width="1.6"/>
          </svg>
          rivera.tomas@correolab.example
        </p>
      </div>
    </div>
  </section>

</main>
</body>
</html>
```